Velnor Group: Business Card for a high end technology company

We need a cool new design for our business cards using our cloud logo. We are a technology consulting business. We pride ourselves on be the best of the best. We mainly focus on cloud solutions and managed services. We need a business card that sets us apart from the other technology companies in the area and allows us to stand out.

Target Market(s)

Technology departments, CIO, CEOs, and Information Technology Staff.

Industry/Entity Type

Information Technology

Contact Information for Business Card

Must have the logo and our name.
Must have employee name, email address, office phone, cell phone and website.
Need to have all info on one side a cool design on backside.

Font styles to use
Serif
Sans Serif

Requirements
Must have
• Must have the logo and our name.
• Must have employee name, email address, office phone, cell phone and website.
• Need to have all info on one side a cool design on back side.
• Must be a crisp clean design, not too busy or confusing.

```html
<!DOCTYPE html>
<html lang="en">
<head>
<meta charset="utf-8">
<title>Velnor Group — Business Card</title>
<link rel="stylesheet" href="https://fonts.googleapis.com/css2?family=Montserrat:wght@400;500&display=swap">
<style>
  :root {
    --backdrop: #e6e7ea;
    --card: #ffffff;
    --ink: #1c1d21;
    --muted: #3a3c42;
    --accent: #1a5fd6;
    --accent-light: #29a9ee;
    --facet-light: #f4f4f5;
    --facet-dark: #dcdde0;
  }
  * { box-sizing: border-box; margin: 0; padding: 0; }
  html, body {
    width: 1200px; height: 900px; overflow: hidden;
    background: var(--backdrop);
    font-family: "Montserrat", sans-serif;
    color: var(--ink);
  }
  .sheet {
    position: relative; width: 1200px; height: 900px;
    display: flex; flex-direction: column; align-items: center; justify-content: center; gap: 50px;
  }
  .card {
    position: relative; width: 600px; height: 343px;
    background: var(--card);
    box-shadow: 0 10px 30px rgba(0,0,0,0.10);
    overflow: hidden;
  }
  /* Front */
  .card-front .wordmark {
    position: absolute; left: 48px; top: 52px;
    font-size: 46px; font-weight: 400; letter-spacing: 1px; color: var(--ink);
  }
  .card-front .person {
    position: absolute; left: 48px; top: 190px;
    font-size: 17px; font-weight: 500; color: var(--ink);
  }
  .card-front .person .divider { color: var(--accent); margin: 0 6px; font-weight: 400; }
  .card-front .person .role { font-size: 12px; font-weight: 400; letter-spacing: 0.5px; }
  .contact-row {
    position: absolute; left: 48px; right: 40px; top: 232px;
    display: flex; gap: 30px; font-size: 13px; color: var(--muted);
  }
  .contact-item { display: flex; align-items: center; gap: 7px; }
  .contact-item svg { width: 15px; height: 15px; flex: none; }
  .rule {
    position: absolute; left: 48px; right: 40px; top: 268px;
    height: 2px; background: var(--accent);
  }
  /* Back */
  .card-back .facets {
    position: absolute; inset: 0;
    background:
      linear-gradient(135deg, var(--facet-light) 0%, var(--facet-dark) 38%, var(--facet-light) 55%, var(--facet-dark) 80%, var(--facet-light) 100%);
  }
  .back-brand {
    position: absolute; inset: 0;
    display: flex; flex-direction: column; align-items: center; justify-content: center; gap: 10px;
  }
  .back-brand .brand-row { display: flex; align-items: center; gap: 16px; }
  .brand-dot {
    width: 46px; height: 46px; border-radius: 50%;
    background: var(--accent-light);
  }
  .back-brand .wordmark { font-size: 44px; font-weight: 400; letter-spacing: 1px; color: var(--ink); }
  .back-brand .website { font-size: 13px; font-weight: 500; letter-spacing: 0.5px; color: var(--ink); }
</style>
</head>
<body>
<main class="sheet">
  <section class="card card-front" aria-label="Business card front">
    <h1 class="wordmark">Velnor Group</h1>
    <p class="person">Dorian Halvers<span class="divider">///</span><span class="role">DIRECTOR</span></p>
    <div class="contact-row">
      <span class="contact-item">
        <svg viewBox="0 0 16 16" aria-hidden="true"><circle cx="8" cy="8" r="8" fill="var(--accent)"/><path d="M5.2 4.2c.4-.3.9-.2 1.1.2l.6 1.2c.2.4 0 .8-.3 1l-.4.3c.4.9 1 1.6 1.9 2.1l.3-.4c.3-.3.7-.4 1-.2l1.2.6c.4.2.5.7.2 1.1l-.5.6c-.4.4-1 .5-1.5.3C6.8 10.2 5.3 8.7 4.6 6.6c-.2-.5 0-1.1.4-1.5z" fill="#fff"/></svg>
        (08) 4720 3916
      </span>
      <span class="contact-item">
        <svg viewBox="0 0 16 16" aria-hidden="true"><circle cx="8" cy="8" r="8" fill="var(--accent)"/><rect x="5.5" y="3.5" width="5" height="9" rx="1" fill="#fff"/><rect x="6.5" y="4.8" width="3" height="5.4" fill="var(--accent)"/></svg>
        (08) 4720 3916
      </span>
      <span class="contact-item">
        <svg viewBox="0 0 16 16" aria-hidden="true"><circle cx="8" cy="8" r="8" fill="var(--accent)"/><rect x="4" y="5" width="8" height="6" rx="0.8" fill="#fff"/><path d="M4.3 5.4 8 8.3l3.7-2.9" stroke="var(--accent)" stroke-width="0.9" fill="none"/></svg>
        admin@velnorgroup.com
      </span>
    </div>
    <div class="rule"></div>
  </section>

  <section class="card card-back" aria-label="Business card back">
    <div class="facets" role="img" aria-label="Soft grey low-poly faceted background pattern"></div>
    <div class="back-brand">
      <div class="brand-row">
        <span class="brand-dot"></span>
        <span class="wordmark">Velnor Group</span>
      </div>
      <span class="website">www.velnorgroup.com</span>
    </div>
  </section>
</main>
</body>
</html>
```